Marketing firm Studio 847
Business card and stationery
Project: Marketing firm Studio 847
Marketing firm Studio 847  -
Creative Brief
Professional
Martin Kovalenko
Marketer, Business Strategist
Derveni, 14, 2385, Strovolia Nicosia Cyprus
Martin@studio-847.com
Www.studio-847.com
I need the logo and the dog on both, business cards and stationery. I need embossed logo or dog but I am also open to other designs.
He logo and the dog but I am also open to new design

```html
<!DOCTYPE html>
<html lang="en">
<head>
<meta charset="utf-8">
<title>Studio 847 — Stationery Set</title>
<link href="https://fonts.googleapis.com/css2?family=Montserrat:wght@600&family=Open+Sans:wght@400;600&display=swap" rel="stylesheet">
<style>
  :root {
    --purple: #9b5aa5;
    --purple-dark: #7e4289;
    --ink: #231f20;
    --paper: #ffffff;
    --frame: #d6d6d6;
    --text: #3a3a3a;
  }
  * { margin: 0; padding: 0; box-sizing: border-box; }
  html, body { width: 1200px; height: 710px; overflow: hidden; background: var(--paper); }
  address { font-style: normal; }
  .sheet {
    position: relative; width: 1200px; height: 710px;
    border: 1px solid var(--frame);
    font-family: "Open Sans", Arial, sans-serif; color: var(--text);
  }
  .piece { position: absolute; overflow: hidden; }
  .piece svg.shape { position: absolute; inset: 0; width: 100%; height: 100%; }
  .brand {
    position: absolute;
    font-family: "Montserrat", Arial, sans-serif; font-weight: 600;
    color: var(--ink); white-space: nowrap; letter-spacing: 0.5px;
    display: flex; align-items: center; gap: 6px;
  }
  .brand .dot { width: 0.45em; height: 0.45em; border-radius: 50%; background: var(--purple); }
  .brand.light { color: var(--paper); }
  .brand.light .dot { background: var(--paper); }

  /* Letterhead */
  .letterhead { left: 24px; top: 19px; width: 522px; height: 666px; background: var(--paper); }
  .letterhead .brand { left: 28px; top: 36px; font-size: 30px; }
  .letterhead-footer {
    position: absolute; left: 28px; bottom: 22px;
    font-size: 8.5px; line-height: 1.45; color: var(--text);
  }
  .letterhead-footer .label { color: var(--purple); }

  /* Business cards */
  .card { width: 211px; height: 125px; border-radius: 4px; }
  .card-contact { left: 552px; top: 24px; background: var(--purple); }
  .card-contact .brand { left: 10px; top: 54px; font-size: 12px; gap: 4px; }
  .card-contact .details {
    position: absolute; left: 124px; right: 6px; top: 12px;
    color: var(--paper); font-size: 5.4px; line-height: 1.5;
  }
  .card-contact .name { font-size: 7.5px; font-weight: 600; }
  .card-contact .role { margin-bottom: 14px; }
  .card-purple { left: 552px; top: 163px; background: var(--purple); }
  .card-purple .brand { left: 38px; top: 44px; font-size: 22px; }
  .card-black { left: 768px; top: 283px; background: var(--ink); }
  .card-black .brand { left: 42px; top: 44px; font-size: 22px; }
  .card-white { left: 984px; top: 283px; background: var(--paper); border: 1px solid var(--frame); }
  .card-white .brand { left: 44px; top: 44px; font-size: 20px; }

  /* Envelope */
  .envelope { left: 559px; top: 427px; width: 636px; height: 258px; background: var(--paper); }
  .envelope .flap-brand { left: 50%; top: 22px; transform: translateX(-50%) rotate(180deg); font-size: 28px; }
  .envelope .return-brand { left: 12px; top: 165px; font-size: 18px; }
  .envelope .return-address { position: absolute; left: 12px; top: 200px; font-size: 7px; }
</style>
</head>
<body>
<main class="sheet">

  <section class="piece letterhead" aria-label="Letterhead">
    <svg class="shape" viewBox="0 0 522 666" preserveAspectRatio="none">
      <path d="M470 0 Q440 333 470 666 L522 666 L522 0 Z" fill="var(--purple)"/>
      <path d="M470 0 Q440 333 470 666" fill="none" stroke="var(--ink)" stroke-width="3"/>
    </svg>
    <div class="brand"><span>Studio 847</span><span class="dot"></span></div>
    <address class="letterhead-footer">
      Derveni, 14, 2385, Strovolia Nicosia Cyprus<br>
      <span class="label">Cell:</span> 00357 99123456 | <span class="label">Phone:</span> 22 555018<br>
      <span class="label">Email:</span> Martin@studio-847.com | Www.studio-847.com
    </address>
  </section>

  <section class="piece card card-contact" aria-label="Business card, contact side">
    <svg class="shape" viewBox="0 0 211 125" preserveAspectRatio="none">
      <path d="M0 0 L100 0 Q120 62 100 125 L0 125 Z" fill="var(--paper)"/>
      <path d="M100 0 Q120 62 100 125" fill="none" stroke="var(--ink)" stroke-width="1.5"/>
    </svg>
    <div class="brand"><span>Studio 847</span><span class="dot"></span></div>
    <div class="details">
      <div class="name">Martin Kovalenko</div>
      <div class="role">Marketer, Business Strategist</div>
      <div>Derveni, 14, 2385, Strovolia</div>
      <div>Nicosia Cyprus</div>
      <div>Cell: 00357 99123456</div>
      <div>Martin@studio-847.com</div>
      <div>Www.studio-847.com</div>
    </div>
  </section>

  <section class="piece card card-purple" aria-label="Business card, logo side">
    <div class="brand light"><span>Studio 847</span><span class="dot"></span></div>
  </section>

  <section class="piece card card-black" aria-label="Business card, dark version">
    <div class="brand light"><span>Studio 847</span><span class="dot"></span></div>
  </section>

  <section class="piece card card-white" aria-label="Business card, light version">
    <div class="brand"><span>Studio 847</span><span class="dot"></span></div>
  </section>

  <section class="piece envelope" aria-label="Envelope">
    <svg class="shape" viewBox="0 0 636 258" preserveAspectRatio="none">
      <path d="M0 0 L636 0 L636 130 Q318 160 0 130 Z" fill="var(--purple)"/>
      <path d="M0 130 Q318 160 636 130" fill="none" stroke="var(--ink)" stroke-width="2"/>
    </svg>
    <div class="brand flap-brand"><span>Studio 847</span><span class="dot"></span></div>
    <div class="brand return-brand"><span>Studio 847</span><span class="dot"></span></div>
    <address class="return-address">Derveni, 14, 2385, Strovolia Nicosia Cyprus</address>
  </section>

</main>
</body>
</html>
```